Plastic Business Cards

I am looking for a plastic business card that matches the theme of my company.

Attached will be logo and template to Prindlecraft for printing.

On card please include the following information:

Logo
612-437-9158 Call or Text
www.GlintvaleCo.com

Window Cleaning
Gutter Cleaning & Covers
Christmas Lighting

200+ 5 Star Reviews

```html
<!DOCTYPE html>
<html lang="en">
<head>
<meta charset="utf-8">
<title>Glintvale Business Card</title>
<link href="https://fonts.googleapis.com/css2?family=Roboto+Condensed:wght@400;700&family=Roboto:wght@400;500;700&display=swap" rel="stylesheet">
<style>
  :root {
    --page-bg: #e7e2da;
    --card-deep: #0b1320;
    --card-mid: #1a2a40;
    --card-glow: #2b4566;
    --name-blue: #1f4f86;
    --text-light: #dfe3e8;
    --text-soft: #c9ccd0;
    --accent-green: #5f9a2c;
    --service-pink: #d8b3b3;
    --service-sand: #d6cbb4;
    --star-orange: #f0921d;
    --divider: rgba(255,255,255,0.18);
  }
  * { margin: 0; padding: 0; box-sizing: border-box; }
  html, body {
    width: 1200px; height: 969px; overflow: hidden;
    background: var(--page-bg);
  }
  .canvas { position: relative; width: 1200px; height: 969px; }
  .card {
    position: absolute; left: 60px; top: 177px;
    width: 1080px; height: 614px; border-radius: 40px; overflow: hidden;
    background:
      radial-gradient(ellipse 60% 70% at 32% 50%, var(--card-glow) 0%, rgba(43,69,102,0) 70%),
      linear-gradient(135deg, var(--card-mid) 0%, var(--card-deep) 75%);
    box-shadow: 0 14px 40px rgba(0,0,0,0.25);
    font-family: "Roboto", Arial, sans-serif;
  }
  .brand {
    position: absolute; left: 140px; top: 262px; height: 80px;
    display: flex; align-items: center; gap: 14px;
  }
  .brand-dot { width: 34px; height: 34px; border-radius: 50%; background: var(--text-light); }
  .brand-name {
    font-family: "Roboto Condensed", sans-serif; font-weight: 700;
    font-size: 64px; color: var(--text-light); letter-spacing: 1px; line-height: 1;
  }
  .divider {
    position: absolute; left: 545px; top: 195px; width: 1px; height: 200px;
    background: var(--divider);
  }
  .contact { position: absolute; left: 583px; top: 208px; }
  .person-name {
    font-family: "Roboto Condensed", sans-serif; font-weight: 700;
    font-size: 46px; color: var(--name-blue); line-height: 1; letter-spacing: 0.5px;
  }
  .person-role { margin-top: 6px; font-size: 23px; color: var(--text-soft); letter-spacing: 0.3px; }
  .contact-lines { margin-top: 32px; }
  .contact-line {
    display: flex; align-items: center; gap: 14px;
    font-size: 24px; color: var(--text-light); height: 31px;
  }
  .contact-line svg { width: 22px; height: 22px; flex: none; }
  .call-note {
    font-family: "Roboto Condensed", sans-serif; color: var(--accent-green); font-size: 26px;
  }
  .reviews { position: absolute; right: 56px; top: 45px; text-align: center; }
  .review-count {
    font-size: 46px; font-weight: 700; color: var(--text-light); line-height: 1;
    margin-left: 20px;
  }
  .review-count .plus { font-weight: 400; }
  .stars { display: flex; gap: 4px; margin-top: 4px; }
  .stars svg { width: 34px; height: 32px; }
  .services {
    position: absolute; left: 0; right: 0; top: 512px;
    display: flex; justify-content: center; align-items: center; gap: 16px;
    font-family: "Roboto Condensed", sans-serif; font-size: 32px;
  }
  .service-a { color: var(--text-soft); }
  .service-b { color: var(--service-pink); }
  .service-c { color: var(--service-sand); }
  .bullet { width: 10px; height: 10px; border-radius: 50%; background: var(--accent-green); }
</style>
</head>
<body>
<div class="canvas">
  <div class="card">
    <div class="reviews">
      <div class="review-count">200<span class="plus">+</span></div>
      <div class="stars" aria-label="Five star reviews">
        <svg viewBox="0 0 24 24"><path fill="var(--star-orange)" d="M12 1.5l3.1 7 7.4.6-5.6 4.9 1.7 7.4L12 17.5 5.4 21.4l1.7-7.4L1.5 9.1l7.4-.6z"/></svg>
        <svg viewBox="0 0 24 24"><path fill="var(--star-orange)" d="M12 1.5l3.1 7 7.4.6-5.6 4.9 1.7 7.4L12 17.5 5.4 21.4l1.7-7.4L1.5 9.1l7.4-.6z"/></svg>
        <svg viewBox="0 0 24 24"><path fill="var(--star-orange)" d="M12 1.5l3.1 7 7.4.6-5.6 4.9 1.7 7.4L12 17.5 5.4 21.4l1.7-7.4L1.5 9.1l7.4-.6z"/></svg>
        <svg viewBox="0 0 24 24"><path fill="var(--star-orange)" d="M12 1.5l3.1 7 7.4.6-5.6 4.9 1.7 7.4L12 17.5 5.4 21.4l1.7-7.4L1.5 9.1l7.4-.6z"/></svg>
        <svg viewBox="0 0 24 24"><path fill="var(--star-orange)" d="M12 1.5l3.1 7 7.4.6-5.6 4.9 1.7 7.4L12 17.5 5.4 21.4l1.7-7.4L1.5 9.1l7.4-.6z"/></svg>
      </div>
    </div>

    <div class="brand">
      <span class="brand-dot"></span>
      <span class="brand-name">Glintvale</span>
    </div>

    <div class="divider"></div>

    <div class="contact">
      <div class="person-name">DANIEL HARTWELL</div>
      <div class="person-role">Managing Director</div>
      <div class="contact-lines">
        <div class="contact-line">
          <svg viewBox="0 0 24 24"><path fill="var(--accent-green)" d="M6.6 10.8a15 15 0 0 0 6.6 6.6l2.2-2.2c.3-.3.7-.4 1-.2 1.1.4 2.3.6 3.6.6.6 0 1 .4 1 1V20c0 .6-.4 1-1 1A17 17 0 0 1 3 4c0-.6.4-1 1-1h3.5c.6 0 1 .4 1 1 0 1.3.2 2.5.6 3.6.1.3 0 .7-.2 1z"/></svg>
          <span>612-437-9158 <span class="call-note">(Call or Text)</span></span>
        </div>
        <div class="contact-line">
          <svg viewBox="0 0 24 24"><circle cx="12" cy="12" r="10" fill="var(--accent-green)"/><path fill="var(--card-deep)" d="M7 6c2 1 3 3 2 5s-3 2-3 4c-1.5-1.5-2-3.5-1.7-5.5C5 8 6 7 7 6zm7 3c2 0 4 1 4 3s-2 3-3 5-3 2-3 0 1-2 0-4 0-4 2-4z"/></svg>
          <span>www.GlintvaleCo.com</span>
        </div>
      </div>
    </div>

    <div class="services">
      <span class="service-a">Window Cleaning</span>
      <span class="bullet"></span>
      <span class="service-b">Gutter Cleaning &amp; Covers</span>
      <span class="bullet"></span>
      <span class="service-c">Christmas Lighting</span>
    </div>
  </div>
</div>
</body>
</html>
```